Harbor Fresh Cleaning car wrap

I need a car wrap design for my work van that is eye catching and stands out. My type of business is carpet cleaning and tile and grout cleaning along with other services. I would like the services to be listed on the wrap along with the phone number and website.
Also please add that we service Commercial and Residential.
Website is:
HarborFreshCleaning.com
Phone number (555) 203-4619
The services I provide are as follow:
Tile & Grout Cleaning
Carpet Cleaning
Hardwood Floor Cleaning and Refinishing
Upholstery and Rug Cleaning
My business colors consist of blue and white but I am open to using other colors.
My logo is attached in the files.
Commercial and Residential
Carpet Cleaning

```html
<!DOCTYPE html>
<html lang="en">
<head>
<meta charset="utf-8">
<title>Harbor Fresh Cleaning – Van Wrap Sides</title>
<link rel="stylesheet" href="https://fonts.googleapis.com/css2?family=Arimo:ital,wght@0,400;0,700;1,400;1,700&display=swap">
<style>
  :root {
    --teal: #3cbdb3;
    --blue: #29a6dc;
    --blue-deep: #1f8fc4;
    --grey: #8c8c8c;
    --ink: #2e2e2e;
    --white: #ffffff;
    --paper: #f4f5f6;
  }
  * { box-sizing: border-box; margin: 0; padding: 0; }
  html, body { width: 990px; height: 1200px; overflow: hidden; background: var(--paper); }
  body { position: relative; font-family: "Arimo", Arial, sans-serif; color: var(--ink); }

  .wrap-side {
    position: absolute; left: 45px; width: 900px; height: 400px;
    border-radius: 28px; overflow: hidden; background: var(--white);
    box-shadow: 0 6px 18px rgba(0,0,0,.12);
  }
  .wrap-side--driver { top: 120px; }
  .wrap-side--passenger { top: 660px; }
  .wrap-side svg.bands { position: absolute; inset: 0; width: 100%; height: 100%; }

  .brand-name {
    position: absolute; font-weight: 700; color: var(--teal);
    font-size: 34px; line-height: 1.1; white-space: nowrap;
  }
  .hood-name {
    position: absolute; font-weight: 700; color: var(--teal);
    font-size: 15px; line-height: 1.1;
  }
  .services { position: absolute; list-style: none; font-size: 15px; line-height: 1.4; white-space: nowrap; }
  .services li { position: relative; }
  .services--left li { padding-left: 22px; }
  .services--left li::before {
    content: ""; position: absolute; left: 0; top: 5px;
    width: 11px; height: 11px; background: var(--teal);
  }
  .services--right { text-align: right; font-style: italic; }
  .services--right li { padding-right: 22px; }
  .services--right li::after {
    content: ""; position: absolute; right: 0; top: 5px;
    width: 11px; height: 11px; background: var(--teal);
  }
  .services li.cont::before, .services li.cont::after { display: none; }

  .website { position: absolute; font-weight: 700; font-size: 17px; color: var(--ink); white-space: nowrap; }
  .audience {
    position: absolute; font-weight: 700; font-size: 27px; color: var(--white);
    letter-spacing: .5px; white-space: nowrap;
  }
  .phone {
    position: absolute; font-weight: 700; font-size: 33px; color: var(--white);
    letter-spacing: .5px; white-space: nowrap;
  }
</style>
</head>
<body>

  <section class="wrap-side wrap-side--driver">
    <svg class="bands" viewBox="0 0 900 400" aria-hidden="true">
      <path d="M0 225 C 200 215, 420 245, 560 238 C 720 230, 850 205, 900 165 L900 400 L0 400 Z" fill="var(--blue)"/>
      <path d="M0 300 L900 300 L900 400 L0 400 Z" fill="var(--blue-deep)" opacity=".18"/>
      <path d="M190 220 C 400 242, 560 236, 690 218 C 800 203, 870 180, 900 150 L900 165 C 850 205, 720 230, 560 238 C 420 245, 280 236, 190 220 Z" fill="var(--grey)"/>
    </svg>
    <div class="hood-name" style="left:40px; top:160px;">Harbor Fresh<br>Cleaning</div>
    <div class="website" style="left:230px; top:185px;">HarborFreshCleaning.com</div>
    <ul class="services services--left" style="left:420px; top:34px;">
      <li>Carpet Cleaning</li>
      <li>Tile &amp; Grout Cleaning</li>
      <li>Upholstery and Rug</li>
      <li class="cont">Cleaning</li>
      <li>Hardwood Floor</li>
      <li class="cont">Cleaning and Refinishing</li>
    </ul>
    <div class="brand-name" style="left:645px; top:50px;">Harbor Fresh<br>Cleaning</div>
    <div class="audience" style="left:360px; top:262px;">Commercial and Residential</div>
    <div class="phone" style="left:430px; top:312px;">(555) 203-4619</div>
  </section>

  <section class="wrap-side wrap-side--passenger">
    <svg class="bands" viewBox="0 0 900 400" aria-hidden="true">
      <g transform="translate(900 0) scale(-1 1)">
        <path d="M0 225 C 200 215, 420 245, 560 238 C 720 230, 850 205, 900 165 L900 400 L0 400 Z" fill="var(--blue)"/>
        <path d="M0 300 L900 300 L900 400 L0 400 Z" fill="var(--blue-deep)" opacity=".18"/>
        <path d="M190 220 C 400 242, 560 236, 690 218 C 800 203, 870 180, 900 150 L900 165 C 850 205, 720 230, 560 238 C 420 245, 280 236, 190 220 Z" fill="var(--grey)"/>
      </g>
    </svg>
    <div class="brand-name" style="left:30px; top:50px;">Harbor Fresh<br>Cleaning</div>
    <ul class="services services--right" style="right:420px; top:34px;">
      <li>Carpet Cleaning</li>
      <li>Tile &amp; Grout Cleaning</li>
      <li>Upholstery and Rug</li>
      <li class="cont">Cleaning</li>
      <li>Hardwood Floor</li>
      <li class="cont">Cleaning and Refinishing</li>
    </ul>
    <div class="website" style="left:455px; top:185px;">HarborFreshCleaning.com</div>
    <div class="hood-name" style="left:770px; top:160px;">Harbor Fresh<br>Cleaning</div>
    <div class="audience" style="left:190px; top:262px;">Commercial and Residential</div>
    <div class="phone" style="left:245px; top:312px;">(555) 203-4619</div>
  </section>

</body>
</html>
```